Proposal Form

Hello! We would like a full color (CMYK) form created with our logo and a similar look and feel to other documents we use (attached). Underneath logo and some design (design should be landscaping based as that is what we will be quoting), we would need a bunch of horizontal lines (for us to write on) and a space in the bottom right which has three lines - (1) Project Total _____________ (2) ______ Monthly Payments of _________________ (3) Pre-pay and receive a 3% discount _______________________

```html
<!DOCTYPE html>
<html lang="en">
<head>
<meta charset="utf-8">
<title>Willow Bend Landscaping – Proposal Form</title>
<link href="https://fonts.googleapis.com/css2?family=Lato:wght@400;700&display=swap" rel="stylesheet">
<style>
  :root {
    --ink: #19191b;
    --brand-green: #3b8a57;
    --soft-green: #c9dfd3;
    --line: #3a3a3a;
    --paper: #ffffff;
    --faint: #e2d6d6;
    --text: #1e1e1e;
  }
  * { margin: 0; padding: 0; box-sizing: border-box; }
  html, body { width: 1200px; height: 848px; overflow: hidden; background: var(--paper); }
  .form-sheet {
    position: relative;
    width: 1200px;
    height: 848px;
    overflow: hidden;
    background: var(--paper);
    font-family: "Lato", Arial, sans-serif;
    color: var(--text);
  }
  .backdrop { position: absolute; inset: 0; width: 100%; height: 100%; }
  .brand-name {
    position: absolute;
    top: 104px;
    left: 0;
    width: 1216px;
    text-align: center;
    color: var(--paper);
    font-weight: 400;
    font-size: 30px;
    letter-spacing: 7px;
    text-transform: uppercase;
  }
  .brand-name--faint {
    top: 796px;
    left: 40px;
    width: 240px;
    font-size: 14px;
    letter-spacing: 3px;
    color: var(--faint);
  }
  .write-line {
    position: absolute;
    height: 0;
    border-top: 1px solid var(--line);
  }
  .summary-box {
    position: absolute;
    left: 726px;
    top: 675px;
    width: 429px;
    height: 158px;
    border: 1.5px solid var(--brand-green);
    border-radius: 12px;
    padding: 16px 19px 0 17px;
    display: flex;
    flex-direction: column;
    gap: 24px;
  }
  .summary-row {
    display: flex;
    align-items: flex-end;
    font-size: 16.5px;
    font-weight: 700;
    font-weight: 400;
    line-height: 20px;
    height: 20px;
    white-space: nowrap;
  }
  .summary-row .label { font-weight: 700; font-weight: 400; padding: 0 3px; }
  .summary-row .label:first-child { padding-left: 0; }
  .blank { border-bottom: 1.5px solid var(--text); height: 16px; }
  .blank--fill { flex: 1; }
  .blank--short { width: 92px; }
</style>
</head>
<body>
<main class="form-sheet">
  <svg class="backdrop" viewBox="0 0 1500 1040" preserveAspectRatio="none" aria-hidden="true">
    <path class="header-band" fill="#3b8a57"
      d="M0,142 C300,262 520,292 700,284 C950,270 1250,170 1500,176 L1500,0 L0,0 Z"/>
    <path class="header-rule" fill="none" stroke="#ffffff" stroke-width="2"
      d="M0,142 C300,258 500,276 700,270 C950,258 1250,140 1500,134"/>
    <path class="header-fill" fill="#19191b"
      d="M0,140 C300,256 500,274 700,268 C950,256 1250,138 1500,132 L1500,0 L0,0 Z"/>
    <path class="lower-swoosh" fill="#c9dfd3"
      d="M0,565 C120,715 260,738 420,738 C700,736 1050,625 1300,622 C1400,621 1460,628 1500,634 L1500,655 C1450,646 1380,639 1300,641 C1050,646 700,774 420,772 C230,770 100,720 0,602 Z"/>
  </svg>

  <div class="brand-name">Willow Bend Landscaping</div>

  <div class="write-line" style="left:296px; top:332px; width:624px;"></div>
  <div class="write-line" style="left:256px; top:372px; width:703px;"></div>
  <div class="write-line" style="left:211px; top:409px; width:793px;"></div>
  <div class="write-line" style="left:256px; top:450px; width:703px;"></div>

  <section class="summary-box">
    <div class="summary-row"><span class="label">Project Title :</span><span class="blank blank--fill"></span></div>
    <div class="summary-row"><span class="blank blank--short"></span><span class="label">Monthly Payment of</span><span class="blank blank--fill"></span></div>
    <div class="summary-row"><span class="label">Pre-pay and receive 3% discount</span><span class="blank blank--fill"></span></div>
  </section>

  <div class="brand-name brand-name--faint">Willow Bend Landscaping</div>
</main>
</body>
</html>
```